Flyer-Design für Ofenservice Firma
Zielgruppe
Die Firma hat als Kerngeschäft Wartung, Reinigung, Reparatur und Inbetriebnahme von Öfen und Kaminen aller Art. Der Fokus liegt dabei auf Pelletöfen. Die Firma versteht sich als zuverlässiger Dienstleister mit gutem Preisleistungsverhältnis. Zielgruppe sind hauptsächlich private Bewohner von Einfamilienhäusern in der ländlichen Gegend (Hessen)
Aufgabenstellung
Zur Bekanntmachung nach Neugründung soll ein Faltflyer gestaltet werden mit insgesamt 6 Bereichen. Die Informationen, welche auf den Flyer sollen, entnehmen Sie bitte dem Entwurf (flyer.pdf). Dieser stellt nur eine erste Idee dar und darf gerne nach Belieben verändert bzw. neu gestaltet werden. Die enthaltenen Informationen, sollten im Großen und Ganzen aber beibehalten werden. Schön wäre evtl. auch eine Hervorhebung der Preise, da wir Preisführer im Markt sind. Auch die Bilder unseres Teams sollen in den Flyer integriert sein. Auf Anfrage kann ich auch gerne weitere Kamin- und Ofenfotos zur Verfügung stellen, für welche ich die Nutzungsrechte habe. Falls Sie weitere Informationen benötigen oder Fragen haben, kommen Sie gerne auf mich zu. Die Bilder dürfen gerne etwas ausgeschnitten werden. Es geht in erster Linie darum, dass die Kunden erkennen, welche Art von Ofen sie zu Hause haben.

```html
<!DOCTYPE html>
<html lang="de">
<head>
<meta charset="utf-8">
<title>Flammwerk Ofenservice – Faltflyer</title>
<link rel="stylesheet" href="https://fonts.googleapis.com/css2?family=Arimo:ital,wght@1,700&family=Roboto+Condensed:ital,wght@0,400;0,700;1,700&display=swap">
<style>
  :root {
    --yellow-deep: #f8d22c;
    --yellow-mid: #fbe04a;
    --yellow-light: #fdea7a;
    --frame: #fdf3b6;
    --text: #4a4a4a;
    --heading: #3e3e3e;
    --label-red: #e0141a;
    --slogan: #565656;
  }
  * { margin: 0; padding: 0; box-sizing: border-box; }
  html, body { width: 848px; height: 1200px; overflow: hidden; background: #fff; }
  body { position: relative; font-family: "Roboto Condensed", "Arial Narrow", sans-serif; color: var(--text); }

  .label {
    position: absolute; transform: translateX(-50%);
    font-family: "Arimo", Arial, sans-serif; font-weight: 700; font-style: italic;
    font-size: 16px; color: var(--label-red); white-space: nowrap;
  }

  .panel {
    position: absolute; left: 33px; width: 757px; overflow: hidden;
    background:
      radial-gradient(ellipse 60% 50% at 30% 20%, rgba(255, 240, 150, .45), transparent 70%),
      linear-gradient(160deg, var(--yellow-light) 0%, var(--yellow-deep) 50%, var(--yellow-mid) 100%);
  }
  .panel--outside { top: 65px; height: 535px; }
  .panel--inside { top: 634px; height: 534px; }

  .col { position: absolute; top: 0; font-size: 10px; line-height: 13px; }
  .abs { position: absolute; }

  .photo {
    position: absolute; background: var(--frame); padding: 9px;
    box-shadow: 0 0 6px rgba(255, 250, 210, .8);
  }
  .photo__fill { width: 100%; height: 100%; }
  .photo__fill--stoves { background: linear-gradient(90deg, #3a2a1c, #8a4a1e 30%, #f3f0ea 50%, #5a3a22 75%, #c9b68a); }
  .photo__fill--team { background: linear-gradient(180deg, #f4f4f4 0%, #d9d9d9 45%, #4a4a4a 100%); }
  .photo__fill--pellet { background: linear-gradient(90deg, #b9d0e6 0%, #e8eef4 40%, #c9c9c9 60%, #f0f0f0 80%, #9a9a9a 100%); }

  .collage { position: absolute; border: 1px solid #c9a93a; background: linear-gradient(120deg, rgba(245, 170, 40, .35), rgba(255, 230, 110, .25)); }

  .col-title { font-weight: 700; font-size: 10.5px; line-height: 13px; color: var(--heading); text-align: center; }
  .section-title { font-weight: 700; font-size: 10.5px; color: var(--heading); }
  .sub-title { font-weight: 700; font-size: 10.5px; color: var(--heading); margin: 13px 0 12px; }

  .bullet { position: relative; padding-left: 5px; }
  .bullet::before { content: "•"; position: absolute; left: 0; }
  .gap { margin-top: 13px; }
  .indent { padding-left: 5px; }
  b { font-weight: 700; }

  .action-title { font-weight: 700; font-size: 16px; color: var(--heading); }

  .brand { text-align: right; font-weight: 700; color: #5c5c5c; }
  .brand__name { display: block; font-size: 22px; line-height: 24px; letter-spacing: 3px; }
  .brand__dot { display: inline-block; width: 12px; height: 12px; border-radius: 50%; background: #5c5c5c; margin-right: 8px; vertical-align: 2px; }
  .brand__sub { display: block; font-size: 12px; line-height: 14px; letter-spacing: 2px; }

  .tagline { font-weight: 700; font-size: 12px; line-height: 15px; text-align: center; color: var(--heading); }
  .slogans { font-weight: 700; font-style: italic; font-size: 15.5px; line-height: 23px; text-align: center; color: var(--slogan); }
  .address { font-weight: 700; font-style: italic; font-size: 10.5px; line-height: 13px; text-align: center; color: var(--slogan); }
</style>
</head>
<body>

  <div class="label" style="left:410px;top:12px">Außenseiten</div>
  <div class="label" style="left:108px;top:43px">Seite 3</div>
  <div class="label" style="left:410px;top:44px">Rückseite</div>
  <div class="label" style="left:659px;top:43px">Seite 1</div>

  <section class="panel panel--outside">
    <div class="col" style="left:26px;width:210px">
      <div class="col-title abs" style="left:0;top:30px;width:196px">Grund-/ Kachelöfen</div>
      <div class="photo" style="left:0;top:59px;width:198px;height:97px">
        <div class="photo__fill photo__fill--stoves" role="img" aria-label="Collage aus Fotos von Kamin- und Kachelöfen"></div>
      </div>
      <div class="abs" style="left:0;top:176px;width:210px">
        <div class="section-title">Leistungsbeschreibung + Preise</div>
        <div class="bullet" style="margin-top:13px">Reinigung Schamott Verkleidung, Sichtscheibe, Zwischenboden, gesamter Feuerraum, sämtliche Rauchgaszüge, Aschebehälter</div>
        <div class="bullet gap">Reinigung der Abgasrohre (bis zu 2 m gestreckte Länge)</div>
        <div class="bullet">Überprüfung der Dichtungen (Türdichtung, Türglasdichtung, Putzdeckeldichtungen)</div>
        <div class="bullet gap">Probelauf des Gerätes</div>
        <div class="indent">Preise Kachelofen mit bis zu 4 Öffnungen<br>Mit Wartungsvertrag: 350€ inkl. MwSt<br>Ohne Wartungsvertrag: 390€ inkl. MwSt<br>Preise Kachelofen mit nachgeschalteter Heizfläche</div>
        <div class="indent gap">Mit Wartungsvertrag: <b>250€</b> inkl. MwSt<br>Ohne Wartungsvertrag: <b>290€</b> inkl. MwSt</div>
      </div>
    </div>

    <div class="col" style="left:272px;width:240px">
      <div class="photo" style="left:0;top:55px;width:197px;height:144px">
        <div class="photo__fill photo__fill--team" role="img" aria-label="Teamfoto der drei Mitarbeiter in schwarzer Arbeitskleidung"></div>
      </div>
      <div class="abs" style="left:0;top:235px">
        <div class="action-title">AKTION</div>
        <div style="margin-top:4px">50 € für Neukundenwerbung<br>( bei Abschluß eines Wartungsvertrages)</div>
      </div>
    </div>

    <div class="col" style="left:535px;width:210px">
      <div class="brand abs" style="left:0;top:75px;width:198px">
        <span class="brand__name"><span class="brand__dot"></span>FLAMMWERK</span>
        <span class="brand__sub">Ofenservice</span>
      </div>
      <div class="photo" style="left:2px;top:131px;width:198px;height:133px">
        <div class="photo__fill photo__fill--team" role="img" aria-label="Teamfoto der drei Mitarbeiter an einem Tisch"></div>
      </div>
      <div class="tagline abs" style="left:-10px;top:290px;width:220px">Ihr kompetenter Servicespezialist<br>für Öfen aller Art</div>
      <div class="slogans abs" style="left:-10px;top:337px;width:220px">Wartung von Öfen aller Art<br>Reparatur, Inbetriebnahme<br>und Beratung<br>Günstige Konditionen</div>
      <div class="address abs" style="left:-10px;top:476px;width:220px">Am Lindenhof 12<br>35398 Talheim<br>06401 / 555 20 40</div>
    </div>
  </section>

  <div class="label" style="left:81px;top:607px">Seite 2</div>
  <div class="label" style="left:408px;top:607px">Innenseiten</div>
  <div class="label" style="left:661px;top:612px">Seite 3</div>

  <section class="panel panel--inside">
    <div class="col" style="left:22px;width:190px">
      <div class="col-title abs" style="left:0;top:20px;width:175px">Pelletöfen</div>
      <div class="photo" style="left:1px;top:51px;width:196px;height:148px">
        <div class="photo__fill photo__fill--pellet" role="img" aria-label="Foto eines weißen Pelletofens vor einem Fenster mit Schneelandschaft"></div>
      </div>
      <div class="abs" style="left:5px;top:222px;width:175px">
        <div>Die Wartung beinhaltet:</div>
        <div class="bullet gap">Reinigung von Sichtscheibe, Brenntopf, Topfhalter, Zwischenboden, gesamter Feuerraum, sämtliche Rauchgaszüge und Aschebehälter</div>
        <div class="bullet gap">Reinigung des Saugzuggebläses Überprüfung und Reinigung des Luftmengensensors</div>
        <div class="bullet gap">Überprüfung der elektrischen Zündung</div>
        <div class="bullet gap">Überprüfung der Dichtungen (Türdichtung, Türglasdichtung, Putzdeckeldichtungen)</div>
        <div class="bullet gap">Überprüfung der Temperaturwächter</div>
        <div class="bullet gap">Probelauf des Gerätes</div>
        <div class="indent gap">Preise<br>Mit Wartungsvertrag: <b>140 €</b> inkl. MwSt<br>Ohne Wartungsvertrag: <b>180 €</b> inkl. MwSt</div>
      </div>
    </div>

    <div class="col" style="left:263px;width:235px">
      <div class="col-title abs" style="left:0;top:20px;width:225px">Scheitholzöfen, Heizkassetten, Brennzellen,<br>Holz- und Küchenherde</div>
      <div class="collage" style="left:5px;top:62px;width:213px;height:101px" role="img" aria-label="Collage aus Fotos von Scheitholzöfen, Heizkassetten und Küchenherden"></div>
      <div class="abs" style="left:0;top:194px;width:180px">
        <div>Die Wartung beinhaltet:</div>
        <div class="bullet gap">Reinigung Schamott Verkleidung, Sichtscheibe, Zwischenboden, gesamter Feuerraum, sämtliche Rauchgaszüge, Aschebehälter</div>
        <div class="bullet gap">Reinigung der Abgasrohre (bis 2 m gestreckte Länge)</div>
        <div class="bullet gap">Überprüfung der Dichtungen (Türdichtung, Türglas-dichtung, Putzdeckeldichtungen) Probelauf des Gerätes</div>
        <div class="indent gap">Preise:<br>Mit Wartungsvertrag: <b>80 €</b> inkl. MwSt<br>Ohne Wartungsvertrag: <b>110 €</b> inkl. MwST</div>
      </div>
    </div>

    <div class="col" style="left:529px;width:214px">
      <div class="section-title abs" style="left:0;top:20px">Firmengeschichte &amp; -profil</div>
      <div class="abs" style="left:0;top:46px;width:214px">
        <p>Als Inhaber geführtes Unternehmen bieten wir professionelle Serviceleistungen rund um Öfen aller Art (Kaminöfen, Pelletöfen, Scheitholzöfen, Kachelöfen, offene Kamine, Grund- und Speicheröfen).</p>
        <p class="gap">Durch erfahrenen Mitarbeitern, regelmäßigen Personalschulungen und Zusammenarbeit mit namhaften Herstellern können wir ihnen eine breite Palette an Dienstleistungen rund um Kaminöfen bieten.</p>
        <p class="gap">Guter Service muss nicht teuer sein! Überzeugen Sie sich von unserem Preis-Leistungs-Verhältnis sowie unseren exklusiven Konditionen bei Abschluss eines Wartungsvertrags<br>Weitere Leistungen:</p>
        <div class="sub-title">Reparatur und Instandsetzung:</div>
        <p>Funktioniert ihr Ofen nicht richtig, sind wir schnellstmöglich für Sie da und setzen ihren Ofen wieder instand.</p>
        <div class="sub-title">Inbetriebnahme:</div>
        <p>Sie haben einen neuen Ofen erworben und möchten sich über die richtige Nutzung und Befeuerung informieren?</p>
        <div class="sub-title">Kaufberatung:</div>
        <p>Sie planen eine Neuanschaffung und möchten sich vorab über Anschlussmöglichkeiten, Brennstoffarten und Modelle informieren? Wir beraten Sie unabhängig und auf Ihre Bedürfnisse zugeschnitten.</p>
      </div>
    </div>
  </section>

</body>
</html>
```